Finance Company need Staff ID card & Patio umbrella design

We need the following design:
1. Employee ID Card (Vertical ID Card)
2. Patio Umbrella
3. Uniform (light grey collar shirt)

Please note that our company theme is grey and gold (yellow). Any mixture is fine as well as long it's simple, nice and unique.

Website: www.hlr-vantor.com.kh
Updates

Project Deadline Extended
Reason: Dear all We would like to extend deadline for 5 days more.

Target Market(s)

Public

Industry/Entity Type

Bank

Requirements
Must have
• 1. ID Card, information needed:
• - Name of the company: HLR Microfinance Ltd
• - Staff name
• - Position
• - ID #
• - Expiry Date
• - Photo
• - Message at the back of ID: This card is property of HLR Mirofinance Ltd. If found, Please return to HLR Microfinance Ltd 023 417 509.
• 2- Patio Umbrella only need company name
• 3- Uniform only need company and color design.
Nice to have
• Gold (or Yellow) and/or grey (Light)

```html
<!DOCTYPE html>
<html lang="en">
<head>
<meta charset="UTF-8">
<title>HLR Microfinance Ltd – Staff ID, Patio Umbrella and Uniform</title>
<link href="https://fonts.googleapis.com/css2?family=Open+Sans:wght@400;600&family=Tinos:wght@400;700&display=swap" rel="stylesheet">
<style>
  :root{
    --stage:#5c6270;
    --gold:#d4ae62;
    --gold-deep:#b07a1a;
    --gold-bright:#e8b820;
    --ink:#3b2c14;
    --white:#ffffff;
    --grey-light:#e6e6e8;
    --grey-mid:#cfcfd2;
    --grey-dark:#9a9aa0;
    --charcoal:#2e2f33;
  }
  *{box-sizing:border-box;margin:0;padding:0}
  html,body{width:1200px;height:750px;overflow:hidden}
  body{background:var(--stage);position:relative;font-family:"Open Sans",sans-serif}

  .id-card{position:absolute;top:60px;width:250px;height:380px;border-radius:18px;overflow:hidden}
  .id-card--front{left:70px;background:var(--gold);color:var(--ink)}
  .id-card--back{left:360px;background:radial-gradient(ellipse at 50% 45%,var(--white) 55%,#f3e6c8 100%);border-bottom:6px solid var(--gold)}

  .staff-photo{position:absolute;left:85px;top:18px;width:80px;height:88px;border:3px solid var(--white);border-radius:14px;background:linear-gradient(160deg,#8a8f98,#3d4048)}
  .brand{position:absolute;top:118px;left:0;width:100%;text-align:center;font-family:"Tinos",serif;color:var(--white);font-size:14px;line-height:1.2;font-weight:400}
  .brand-dot{display:block;width:30px;height:30px;border-radius:50%;background:var(--gold-bright);margin:0 auto 8px}
  .staff-details{position:absolute;top:205px;left:22px;right:14px;font-size:9.5px;display:grid;grid-template-columns:78px 14px 1fr;row-gap:6px}
  .staff-details dt{grid-column:1}
  .staff-details .sep{grid-column:2}
  .staff-details dd{grid-column:3}
  .signatory{position:absolute;right:12px;bottom:10px;font-size:9px;color:var(--white)}

  .back-seal{position:absolute;left:70px;top:95px;width:110px;height:110px;border-radius:50%;background:#f2ead8;opacity:.8}
  .return-note{position:absolute;left:0;right:0;bottom:36px;text-align:center;font-size:9.5px;line-height:1.9;color:var(--gold-deep);padding:0 18px}

  .umbrella{position:absolute;left:740px;top:25px;width:380px;height:360px}
  .umbrella text{font-family:"Tinos",serif;fill:#6e6e74}

  .uniform{position:absolute;left:590px;top:410px;width:520px;height:300px}
  .uniform text{font-family:"Tinos",serif;fill:var(--charcoal)}
</style>
</head>
<body>

<section class="id-card id-card--front" aria-label="Staff ID card, front">
  <div class="staff-photo" role="img" aria-label="Staff portrait photo"></div>
  <h1 class="brand"><span class="brand-dot"></span>HLR<br>MICROFINANCE LTD</h1>
  <dl class="staff-details">
    <dt>Name</dt><span class="sep">:</span><dd>Daren Kosal</dd>
    <dt>Designation</dt><span class="sep">:</span><dd>Manager</dd>
    <dt>ID Number</dt><span class="sep">:</span><dd>123456</dd>
    <dt>D.O.B.</dt><span class="sep">:</span><dd>07/08/1983</dd>
    <dt>Address</dt><span class="sep">:</span><dd>14 sample 2200</dd>
    <dt>Date of Issuing</dt><span class="sep">:</span><dd>11/06/2016</dd>
    <dt>Expiry Date</dt><span class="sep">:</span><dd>10/06/2017</dd>
  </dl>
  <p class="signatory">Authorised Signatory</p>
</section>

<section class="id-card id-card--back" aria-label="Staff ID card, back">
  <div class="back-seal"></div>
  <p class="return-note">This card is property of HLR Mirofinance Ltd.<br>If found, Please return to HLR Microfinance Ltd<br>023 417 509.</p>
</section>

<svg class="umbrella" viewBox="0 0 380 360" aria-label="Patio umbrella canopy design">
  <line x1="190" y1="90" x2="190" y2="330" stroke="#c9c9cc" stroke-width="4"/>
  <rect x="150" y="322" width="80" height="30" fill="var(--charcoal)"/>
  <path d="M190 6 L10 72 L18 102 Q100 110 190 104 Q280 110 362 102 L370 72 Z" fill="var(--grey-light)"/>
  <path d="M10 72 L18 102 Q100 110 190 104 Q280 110 362 102 L370 72 Q280 80 190 76 Q100 80 10 72Z" fill="var(--grey-mid)"/>
  <line class="panel-seam" x1="108" y1="77" x2="110" y2="107" stroke="#bdbdc2" stroke-width="1"/>
  <line class="panel-seam" x1="272" y1="77" x2="270" y2="107" stroke="#bdbdc2" stroke-width="1"/>
  <circle cx="190" cy="64" r="7" fill="var(--gold-bright)"/>
  <text x="190" y="96" text-anchor="middle" font-size="12" font-weight="700">HLR MICROFINANCE LTD</text>
  <circle cx="60" cy="70" r="5" fill="var(--gold-bright)"/>
  <text x="60" y="94" text-anchor="middle" font-size="7">HLR MICROFINANCE LTD</text>
  <circle cx="322" cy="72" r="4" fill="var(--gold-bright)"/>
  <text x="322" y="94" text-anchor="middle" font-size="5.5">HLR MICROFINANCE</text>
</svg>

<svg class="uniform" viewBox="0 0 520 300" aria-label="Light grey polo uniform, front and back">
  <g class="polo polo--front">
    <path d="M85 10 L140 10 Q150 30 165 10 L220 10 L280 60 L260 120 L225 110 L225 290 L80 290 L80 110 L45 120 L25 60 Z" fill="var(--grey-light)"/>
    <path d="M115 10 L152 60 L140 70 L110 30 Z M190 10 L152 60 L164 70 L195 30 Z" fill="var(--grey-mid)"/>
    <rect x="146" y="50" width="14" height="70" fill="var(--gold)"/>
    <circle cx="153" cy="70" r="2.5" fill="var(--grey-dark)"/>
    <circle cx="153" cy="90" r="2.5" fill="var(--grey-dark)"/>
    <rect x="80" y="260" width="6" height="30" fill="var(--gold)"/>
    <rect x="219" y="260" width="6" height="30" fill="var(--gold)"/>
    <circle cx="110" cy="87" r="5" fill="var(--gold-bright)"/>
    <text x="110" y="103" text-anchor="middle" font-size="5">HLR MICROFINANCE LTD</text>
  </g>
  <g class="polo polo--back">
    <path d="M355 10 L440 10 L495 60 L478 120 L445 110 L445 290 L350 290 L350 110 L317 120 L300 60 Z" fill="var(--grey-light)"/>
    <rect x="355" y="8" width="85" height="12" rx="4" fill="var(--grey-mid)"/>
  </g>
</svg>

</body>
</html>
```